New Company Business Card Design

I have a new company logo and I want a new business card design. I dont know if the logo file i attached is in the correct format or quality. We are a New York City Specialty construction Firm specializing in high risk out of the box projects. I want a simple and classy business card that people will his card is as crisp as the work his company does.

Target Market(s)

Clients in the heavy construction industry in New York City

Industry/Entity Type

Construction Company

Contact Information for Business Card

Simple Classy - DIFFERENT

Font styles to use
Other font styles liked:
• Mach the logo font in some way

Colors

Designer to choose colors to be used in the design.

Requirements
Must have
• Uniqueness
Nice to have
• Nothing particular - Just different and classy - Timeless
Should not have
• Goofy Shit or Gimmicky shit

```html
<!DOCTYPE html>
<html lang="en">
<head>
<meta charset="utf-8">
<title>Halvern Associates – Business Card</title>
<link rel="stylesheet" href="https://fonts.googleapis.com/css2?family=Montserrat:wght@500;600;800&family=Nunito+Sans:wght@400&display=swap">
<style>
  :root{
    --page:#ededed;
    --brand-blue:#0b6fc8;
    --brand-blue-dark:#0a5fb0;
    --card-white:#ffffff;
    --card-dark:#1b1b1b;
    --ink:#1a1a1a;
    --rule:#2a2a2a;
  }
  html,body{margin:0;padding:0;width:1200px;height:1200px;overflow:hidden;background:var(--page);}
  .card{position:absolute;left:155px;width:890px;height:486px;overflow:hidden;box-shadow:0 18px 40px rgba(0,0,0,.28);}
  .card--front{top:78px;background:var(--card-white);}
  .card--back{top:637px;background:var(--card-dark);}
  .band{position:absolute;left:0;width:890px;height:32px;display:block;}
  .band--top{top:0;}
  .band--bottom{bottom:0;transform:scaleY(-1);}
  .band__fill{fill:var(--brand-blue);}

  .brand{position:absolute;font-family:"Montserrat",sans-serif;font-weight:800;color:var(--brand-blue);text-transform:uppercase;margin:0;}
  .brand--front{left:70px;top:190px;width:280px;font-size:30px;line-height:1.15;letter-spacing:2px;text-align:center;}
  .brand--back{left:0;right:0;top:170px;font-size:54px;line-height:1.2;letter-spacing:6px;text-align:center;}

  .divider{position:absolute;left:444px;top:110px;width:2px;height:268px;background:var(--rule);}

  .contact{position:absolute;left:490px;top:166px;}
  .contact__name{margin:0 0 12px;font-family:"Montserrat",sans-serif;font-weight:600;font-size:31px;letter-spacing:1.6px;color:var(--ink);}
  .contact__list{list-style:none;margin:0;padding:0;font-family:"Nunito Sans",sans-serif;font-size:16px;color:var(--ink);line-height:21px;}
  .contact__item{display:flex;align-items:flex-start;gap:7px;margin-bottom:8px;}
  .contact__icon{width:18px;height:18px;flex:none;margin-top:2px;fill:var(--ink);}
</style>
</head>
<body>

<section class="card card--front">
  <svg class="band band--top" viewBox="0 0 890 32" preserveAspectRatio="none" aria-hidden="true">
    <path class="band__fill" d="M0 0H890V31H632L598 16H292L258 31H0Z"/>
  </svg>

  <p class="brand brand--front">Halvern<br>Associates, Inc.</p>

  <div class="divider"></div>

  <div class="contact">
    <h1 class="contact__name">MARCUS T. BELLAMY</h1>
    <ul class="contact__list">
      <li class="contact__item">
        <svg class="contact__icon" viewBox="0 0 24 24" aria-hidden="true"><path d="M6.6 10.8c1.4 2.8 3.8 5.1 6.6 6.6l2.2-2.2c.3-.3.7-.4 1-.2 1.1.4 2.3.6 3.6.6.6 0 1 .4 1 1V20c0 .6-.4 1-1 1C10.6 21 3 13.4 3 4c0-.6.4-1 1-1h3.5c.6 0 1 .4 1 1 0 1.3.2 2.5.6 3.6.1.3 0 .7-.2 1z"/></svg>
        <span>555-014-2287</span>
      </li>
      <li class="contact__item">
        <svg class="contact__icon" viewBox="0 0 24 24" aria-hidden="true"><path d="M2 5h20v14H2zM4 7v.4l8 5.2 8-5.2V7zm0 2.8V17h16V9.8l-8 5.2z"/></svg>
        <span>marcus@halvern.com</span>
      </li>
      <li class="contact__item">
        <svg class="contact__icon" viewBox="0 0 24 24" aria-hidden="true"><path d="M12 2a7 7 0 0 0-7 7c0 5.2 7 13 7 13s7-7.8 7-13a7 7 0 0 0-7-7zm0 9.5A2.5 2.5 0 1 1 12 6.5a2.5 2.5 0 0 1 0 5z"/></svg>
        <span>118 Harbor Lane -<br>Riverton, New Jersey 07090</span>
      </li>
    </ul>
  </div>

  <svg class="band band--bottom" viewBox="0 0 890 32" preserveAspectRatio="none" aria-hidden="true">
    <path class="band__fill" d="M0 0H890V31H632L598 16H292L258 31H0Z"/>
  </svg>
</section>

<section class="card card--back">
  <svg class="band band--top" viewBox="0 0 890 32" preserveAspectRatio="none" aria-hidden="true">
    <path class="band__fill" d="M0 0H890V31H632L598 16H292L258 31H0Z"/>
  </svg>

  <p class="brand brand--back">Halvern<br>Associates, Inc.</p>

  <svg class="band band--bottom" viewBox="0 0 890 32" preserveAspectRatio="none" aria-hidden="true">
    <path class="band__fill" d="M0 0H890V31H632L598 16H292L258 31H0Z"/>
  </svg>
</section>

</body>
</html>
```